Business Card Design

we pay more for your estate jewelry .

Industry/Entity Type

Jewelry

Contact Information for Business Card

ray's coin and bullion llc .we buy gold , silver ,coins and diamonds.742 willow creek road cedar hollow pa 08099. 610-555-0148. open 7 days 10 to 6

```html
<!DOCTYPE html>
<html lang="en">
<head>
<meta charset="utf-8">
<title>Ray's Coin and Bullion LLC – Business Card</title>
<link rel="stylesheet" href="https://fonts.googleapis.com/css2?family=Oswald:wght@500&display=swap">
<style>
  :root {
    --backdrop: #d9d9d9;
    --frame: #333132;
    --paper: #ffffff;
    --gold: #f0b92d;
    --ink: #333132;
  }
  html, body {
    margin: 0;
    padding: 0;
    width: 1200px;
    height: 1000px;
    overflow: hidden;
    background: var(--backdrop);
  }
  .canvas {
    position: relative;
    width: 1200px;
    height: 1000px;
    display: flex;
    align-items: center;
    justify-content: center;
  }
  .business-card {
    width: 1000px;
    height: 572px;
    box-sizing: border-box;
    background: var(--frame);
    padding: 36px;
    box-shadow: 0 6px 18px rgba(0,0,0,0.25);
  }
  .card-face {
    width: 100%;
    height: 100%;
    background: var(--paper);
    display: flex;
    align-items: center;
    box-sizing: border-box;
    padding: 0 48px 0 60px;
    font-family: 'Oswald', sans-serif;
    font-weight: 500;
    text-transform: uppercase;
  }
  .brand {
    flex: 0 0 420px;
    display: flex;
    align-items: center;
    gap: 22px;
  }
  .brand-dot {
    flex: 0 0 64px;
    height: 64px;
    border-radius: 50%;
    background: var(--gold);
  }
  .brand-name {
    color: var(--ink);
    font-size: 40px;
    line-height: 1.15;
    letter-spacing: 0.5px;
  }
  .details {
    flex: 1;
    padding-left: 30px;
    font-size: 31px;
    line-height: 1.3;
    letter-spacing: 0.5px;
  }
  .details p {
    margin: 0;
    white-space: nowrap;
  }
  .tagline { color: var(--gold); margin-bottom: 6px !important; }
  .contact { color: var(--ink); }
</style>
</head>
<body>
<main class="canvas">
  <section class="business-card">
    <div class="card-face">
      <div class="brand">
        <span class="brand-dot" aria-hidden="true"></span>
        <span class="brand-name">Ray's Coin and Bullion LLC</span>
      </div>
      <div class="details">
        <p class="tagline">We buy gold . silver .<br>coins and diamonds</p>
        <p class="contact">742 Willow Creek Road</p>
        <p class="contact">Cedar Hollow PA 08099</p>
        <p class="contact">610-555-0148</p>
        <p class="contact">Open 7 days 10 to 6</p>
      </div>
    </div>
  </section>
</main>
</body>
</html>
```